Harbin waste and recycling needs a thank you for business card

We need to design a thank you card for our customers who purchase with us. I like black gloss front and back with thankyou on the front. Or white gloss front back.
The inside should be white and maybe our logo on the bottom right hand side (as you open it up). Maybe put some more pictures on it.

On the inside of the card write -
Congratulations on your recent purchase.
Customers like YOU are the foundation of our business.
We appreciate having YOU as a customer and we look forward to providing you with the best possible service into the future.

PS as an added value if you refer any purchasing clients to Harbin YOU will receive one years free document destruction to the value of $204 or $164 towards a waste and recycling credit. Prices include GST.

Warm Regards,

Dorian Palkett, Business Owner.

Target Market(s)

Business customers within Australia

Industry/Entity Type

Recycling

Colors

Designer to choose colors to be used in the design.

Requirements
Must have
• 'thank you' on the front

'Congratulations on your recent purchase..........' exact text as in project overview. This is to appear on the inside page.

Our logo to be small on the bottom of the inside somewhere
Nice to have
• some more of our pictures

```html
<!DOCTYPE html>
<html lang="en">
<head>
<meta charset="utf-8">
<title>Harbin Waste &amp; Recycling – Thank You Card</title>
<link rel="stylesheet" href="https://fonts.googleapis.com/css2?family=Allerta+Stencil&family=Delius&display=swap">
<style>
  :root {
    --page-bg: #ffffff;
    --card-black: #000000;
    --card-white: #ffffff;
    --frame-grey: #9a9a9a;
    --mark-grey: #5a5a5a;
    --mark-dark: #2a2a2a;
    --headline-white: #ffffff;
    --message-teal: #137f86;
    --body-grey: #4a4a4a;
  }
  html, body {
    margin: 0;
    padding: 0;
    width: 1200px;
    height: 1031px;
    overflow: hidden;
    background: var(--page-bg);
  }
  .spread {
    position: absolute;
    top: 337px;
    left: 76px;
    display: flex;
    gap: 54px;
  }
  .card-front,
  .card-inside {
    width: 510px;
    height: 357px;
    position: relative;
    box-sizing: border-box;
  }
  /* Front cover */
  .card-front {
    background: var(--card-black);
    overflow: hidden;
  }
  .recycle-mark {
    position: absolute;
    left: 105px;
    top: 18px;
    width: 290px;
    height: 318px;
    border-radius: 50%;
    background: radial-gradient(circle at 50% 45%, var(--mark-grey) 0%, var(--mark-dark) 55%, var(--card-black) 75%);
    opacity: 0.9;
  }
  .front-title {
    position: absolute;
    left: 0;
    right: 0;
    top: 140px;
    margin: 0;
    text-align: center;
    font-family: "Allerta Stencil", sans-serif;
    font-weight: 400;
    font-size: 64px;
    letter-spacing: 1px;
    color: var(--headline-white);
    line-height: 1;
  }
  /* Inside page */
  .card-inside {
    background: var(--card-white);
    border: 1px solid var(--frame-grey);
    padding: 40px 34px 0 52px;
    font-family: "Delius", sans-serif;
  }
  .message {
    margin: 0 0 12px;
    text-align: center;
    color: var(--message-teal);
    font-size: 14.5px;
    line-height: 1.2;
    padding-right: 18px;
  }
  .postscript {
    margin: 22px 0 14px;
    color: var(--body-grey);
    font-size: 11.5px;
    line-height: 1.3;
  }
  .postscript .ps-lead { font-size: 14px; }
  .sign-off {
    display: flex;
    justify-content: space-between;
    align-items: flex-start;
  }
  .signature {
    color: var(--body-grey);
    font-size: 12.5px;
    line-height: 1.3;
    width: 190px;
  }
  .signature p { margin: 0 0 12px; }
  .brand {
    display: flex;
    align-items: center;
    gap: 8px;
    margin-top: 10px;
    color: var(--body-grey);
    font-size: 14px;
    line-height: 1.1;
  }
  .brand-square {
    width: 30px;
    height: 30px;
    background: var(--message-teal);
  }
</style>
</head>
<body>
  <main class="spread">
    <section class="card-front" aria-label="Card front">
      <div class="recycle-mark" role="img" aria-label="Large grey recycling arrows symbol"></div>
      <h1 class="front-title">THANK YOU</h1>
    </section>

    <section class="card-inside" aria-label="Card inside">
      <p class="message">Congratulations on your recent purchase.</p>
      <p class="message">Customers like YOU are the foundation of our business.</p>
      <p class="message">We appreciate having YOU as a customer and we look forward to providing you with the best possible service into the future.</p>

      <p class="postscript"><span class="ps-lead">PS</span> as an added value if you refer any purchasing clients to Harbin YOU will receive one years free document destruction to the value of $204 or $164 towards a waste and recycling credit. Prices include GST.</p>

      <div class="sign-off">
        <div class="signature">
          <p>Warm regards,</p>
          <p>Dorian Palkett, Business Owner</p>
        </div>
        <div class="brand">
          <span class="brand-name">HARBIN<br>WASTE &amp; RECYCLING</span>
          <span class="brand-square"></span>
        </div>
      </div>
    </section>
  </main>
</body>
</html>
```